Vexa Wellness Business Card

A Double Sided Business Card

I am a private company in Melbourne, Australia, working in the Health industry. I am a nutritionist and lifestyle coach, whom specialises in using raw foods ie. fruits/nuts/vegetables to help heal my clients and enable them to achieve their ultimate state of health.

I want a sophisticated design and colour for my card that appeals to both men and women from teenage through to elderly.

Front of Card:

Red apple peel spiral in the shape of an apple. I would like a leaf/leaves coming off the stem of the apple. Please see attachments for example.

***On Right Hand side of Image is business Name: Vexa Wellness

Underneath LOGO use slogan " Let Food Be Your Medicine"

***Use Deep Red and Blues for Text Colouring

Back of Card:

Marisol Tenzing
Nutritional Specialist and Lifestyle Coach

Specialising in: Diseased Conditions
Weight Management
Achieving your Ultimate State of Health

enquiries@vexawellness.example 0493 517 642

**Make sure the front design of the card flows onto the back.
Updates

Email address has been amended, Also more specific details have been given for apple peel Image, and another image attached as example of Leaf on stem of apple.

I little more insight into what sort of feel were trying to create. We're apart of the health industry, and we want the card to have a medical/clinical feeling about it.

Target Market(s)

Males and Females from teenages to elderly

Industry/Entity Type

Business

Requirements
Must have
• Red Apple Peel Spiral, in the shape of an apple, with a leaf/leaves attached to stem.
***Must be in the shape of an apple
***Please use coloring on inside of apple peel to resemble inside of an apple.
Nice to have
• I would like my card to have a clinical feel.
Should not have
• We don't want the image of the apple to look like a Christmas decoration

```html
<!DOCTYPE html>
<html lang="en">
<head>
<meta charset="utf-8">
<title>Marisol Tenzing – Business Card</title>
<link rel="stylesheet" href="https://fonts.googleapis.com/css2?family=Quicksand:wght@500;600&display=swap">
<style>
  :root {
    --card-bg: #ffffff;
    --swoosh: #ececef;
    --swoosh-deep: #e2e2e6;
    --band-blue: #3a5bb8;
    --band-green: #7dbb3c;
    --band-red: #e0262b;
    --name-red: #e0282e;
    --title-navy: #2b2b5e;
    --body-ink: #1e1e24;
    --apple-red: #d8242a;
    --apple-dark: #9e1318;
    --apple-flesh: #f2eee8;
  }
  html, body {
    margin: 0;
    padding: 0;
    overflow: hidden;
    background: #ffffff;
  }
  .card {
    position: relative;
    width: 1200px;
    height: 741px;
    background: var(--card-bg);
    overflow: hidden;
    font-family: "Quicksand", sans-serif;
  }
  .card-bands {
    position: absolute;
    inset: 0;
    width: 1200px;
    height: 741px;
  }
  .identity {
    position: absolute;
    left: 0;
    width: 1200px;
    top: 172px;
    text-align: center;
  }
  .person-name {
    margin: 0;
    color: var(--name-red);
    font-weight: 500;
    font-size: 50px;
    line-height: 1;
  }
  .person-role {
    margin: 12px 0 0;
    color: var(--title-navy);
    font-weight: 600;
    font-size: 33px;
    line-height: 1.25;
  }
  .specialties {
    position: absolute;
    left: 0;
    width: 1200px;
    top: 370px;
    text-align: center;
  }
  .specialties-heading {
    margin: 0;
    color: var(--title-navy);
    font-weight: 500;
    font-size: 37px;
    line-height: 1.1;
  }
  .specialties-list {
    margin: 12px 0 0;
    color: var(--body-ink);
    font-weight: 500;
    font-size: 29px;
    line-height: 1.55;
  }
  .apple-art {
    position: absolute;
    left: 944px;
    top: 232px;
    width: 200px;
    height: 244px;
  }
  .contact {
    position: absolute;
    top: 618px;
    left: 214px;
    display: flex;
    align-items: center;
    gap: 26px;
    color: var(--title-navy);
    font-weight: 500;
    font-size: 31px;
  }
  .contact-item {
    display: flex;
    align-items: center;
    gap: 8px;
  }
  .contact-icon {
    width: 40px;
    height: 40px;
    flex: none;
  }
</style>
</head>
<body>
<div class="card">
  <svg class="card-bands" viewBox="0 0 1200 741" aria-hidden="true">
    <path fill="var(--swoosh)" d="M0 300 Q 500 430 1200 330 L1200 560 Q 600 600 0 520 Z"/>
    <path fill="var(--swoosh-deep)" d="M0 420 Q 520 500 1200 430 L1200 560 Q 600 600 0 530 Z" opacity="0.6"/>
    <path fill="var(--swoosh)" d="M0 160 Q 700 40 1200 190 L1200 240 Q 700 110 0 230 Z" opacity="0.7"/>
    <path fill="none" stroke="var(--band-blue)" stroke-width="18" d="M-20 82 Q 600 -72 1220 96"/>
    <path fill="none" stroke="var(--band-green)" stroke-width="7" d="M-20 152 Q 600 56 1220 160"/>
    <path fill="none" stroke="var(--band-red)" stroke-width="14" d="M-20 548 Q 600 612 1220 556"/>
    <path fill="none" stroke="var(--band-blue)" stroke-width="16" d="M-20 590 Q 600 805 1220 594"/>
  </svg>

  <header class="identity">
    <h1 class="person-name">Marisol Tenzing</h1>
    <p class="person-role">Nutritional Specialist<br>Lifestyle Coach</p>
  </header>

  <section class="specialties">
    <h2 class="specialties-heading">Specialising in:</h2>
    <p class="specialties-list">·Diseased Conditions ·Weight Management<br>·Achieving your Ultimate State of Health</p>
  </section>

  <svg class="apple-art" viewBox="0 0 200 244" role="img" aria-label="Red apple peel spiral forming an apple shape, with a green leaf on the stem">
    <defs>
      <radialGradient id="apple-tone" cx="40%" cy="40%" r="65%">
        <stop offset="0" stop-color="var(--apple-red)"/>
        <stop offset="0.7" stop-color="var(--apple-red)"/>
        <stop offset="1" stop-color="var(--apple-dark)"/>
      </radialGradient>
    </defs>
    <ellipse cx="100" cy="126" rx="90" ry="96" fill="url(#apple-tone)"/>
    <ellipse cx="100" cy="236" rx="60" ry="6" fill="#dcdce0"/>
  </svg>

  <footer class="contact">
    <span class="contact-item">
      <svg class="contact-icon" viewBox="0 0 40 40" aria-hidden="true">
        <circle cx="20" cy="20" r="19" fill="var(--band-red)"/>
        <g fill="none" stroke="#fff" stroke-width="2">
          <circle cx="20" cy="20" r="11"/>
          <ellipse cx="20" cy="20" rx="5" ry="11"/>
          <line x1="9" y1="20" x2="31" y2="20"/>
        </g>
      </svg>
      enquiries@vexawellness.example
    </span>
    <span class="contact-item">
      <svg class="contact-icon" viewBox="0 0 40 40" aria-hidden="true">
        <circle cx="20" cy="20" r="19" fill="var(--band-red)"/>
        <path fill="#fff" d="M13 10 l5 -1 3 7 -3 2 q2 5 6 7 l2 -3 7 3 -1 5 q-3 2 -7 1 q-9 -4 -13 -14 q-1 -4 1 -7 z"/>
      </svg>
      0493 517 642
    </span>
  </footer>
</div>
</body>
</html>
```